Record Sales in.. La Jolla | California

We need a CLEAN and MODERN looking flyer for a property. SIMPLE but CLEAN and cutting edge. We would like to use the logo attached at the bottom of the page. We prefer to only have the flyer front and back. If its necessary - we can do 2 pages.

--

Below is the Information/Stats we would like to include:

4318 Heron Court, La Jolla, CA | "The Cedar Loft"
- 4th Highest Sale in History of La Jolla's Highly Desirable Fern Hollow Community
- Recognized Internationally as a "One-of-a-Kind" Architectural Masterpiece
- Featured on Real Estate TV Show "Coastal Prestige Homes"

3814 Vereda Lumo, La Jolla, CA | Marisol Heights
- 2nd Highest Sale Price
- 3rd Highest Price Per S/F since 1997
- Extensive Pre-MLS Marketing. Sold on Day 1 of Listing

Client Testimonials:

4318 Heron Court
"Ned sold my oceanfront home in La Jolla and literally found the 'needle- in-the-hay-stack' cash buyer through his smart and targeted marketing backed by top notch Whitcombe Global Estates. He is an excellent communicator and negotiator and stays the course through thick and thin until a property is sold, while never losing focus on his #1 goal: to make his client happy. Definitely my agent of choice for any future transaction (buy or sell) and he should be yours too."

3814 Vereda Lumo
"We feel so lucky and fortunate to have found Ned. He promised me he would handle our sale from beginning to the end. Not only did Ned keep his promise, he went above & beyond to make sure the transaction stays at its course and time. Ned far exceeded our expectations in the price of the sale. I definitely will recommend Ned to all my family and friends. Thank you, Ned for an amazing experience."

--

Also include the Agents name and Contact Information below our logo:
- Ned Falworth | (858) 555-0172 | Ned@HOMQ-VT.example

Target Market(s)

Luxury Real Estate

Industry/Entity Type

Property

Colors

Designer to choose colors to be used in the design.

Requirements
Nice to have
• Unique & Modern Design

```html
<!DOCTYPE html>
<html lang="en">
<head>
<meta charset="utf-8">
<title>Record Sales – La Jolla</title>
<link href="https://fonts.googleapis.com/css2?family=Maven+Pro:wght@400;500;700&display=swap" rel="stylesheet">
<style>
:root{
  --navy:#273261;
  --sky:#4da2e3;
  --paper:#ffffff;
  --backdrop:#2c2c2e;
  --ink:#2a3360;
}
*{box-sizing:border-box;margin:0;padding:0}
html,body{width:1200px;height:1200px;overflow:hidden;background:var(--backdrop);font-family:"Maven Pro",sans-serif}
.flyer{position:absolute;top:262px;width:523px;height:676px;background:var(--paper);overflow:hidden}
.flyer--front{left:74px}
.flyer--back{left:602px}
.title-bar{position:absolute;left:31px;top:26px;width:174px;height:32px;background:var(--navy)}
.title{position:absolute;left:214px;top:24px;font-size:36px;font-weight:700;color:var(--navy);letter-spacing:0;line-height:1;white-space:nowrap}
.address{position:absolute;left:32px;top:96px;font-size:19.5px;font-weight:500;color:var(--ink);line-height:23px}
.testimonial{position:absolute;left:250px;top:76px;width:244px;font-size:7.2px;font-style:italic;color:var(--ink);line-height:10.3px;text-align:justify}
.testimonial::before{content:"\201C";font-style:normal;font-weight:700;font-size:20px;position:absolute;left:-15px;top:-3px;line-height:1}
.photo{position:absolute}
.photo--hero{left:31px;top:167px;width:306px;height:256px}
.photo--left{left:31px;top:430px;width:246px;height:128px}
.photo--right{left:282px;top:430px;width:211px;height:128px}
.highlights{position:absolute;left:342px;top:167px;width:151px;height:256px;background:var(--navy);color:#fff;padding:20px 10px 0 10px}
.highlights h2{font-size:16px;font-weight:700;line-height:19px;color:var(--sky);margin-bottom:8px;text-transform:uppercase}
.highlights h2 .plain{color:#fff}
.highlights ul{list-style:none}
.highlights li{position:relative;padding-left:16px;font-size:9.8px;line-height:14.5px;margin-bottom:3px}
.highlights li svg{position:absolute;left:0;top:2px;width:10px;height:10px}
.flyer--back .highlights{padding-top:50px}
.flyer--back .highlights h2{margin-bottom:14px}
.flyer--back .highlights li{margin-bottom:12px}
.brand{position:absolute;left:34px;top:588px;color:var(--navy);font-weight:500;line-height:1}
.brand .group{font-size:24px;display:block}
.brand .partner{display:flex;align-items:center;gap:8px;margin-top:8px;font-size:12px;padding-left:76px}
.brand .divider{width:1px;height:18px;background:var(--navy)}
.contact-band{position:absolute;left:284px;top:570px;width:239px;height:106px;background:var(--navy);clip-path:polygon(36px 0,100% 0,100% 100%,0 100%)}
.contact{position:absolute;left:324px;top:590px;color:#fff;font-size:15px;line-height:19px;white-space:nowrap}
.contact div{display:flex;align-items:center;gap:5px}
.contact .phone{font-weight:700}
.contact svg{width:12px;height:12px;flex:none}
</style>
</head>
<body>

<svg width="0" height="0" style="position:absolute">
  <defs>
    <symbol id="tick" viewBox="0 0 10 10"><circle cx="5" cy="5.2" r="4" fill="none" stroke="#fff" stroke-width="1.1"/><path d="M3 5.2l1.7 1.6L9 2" fill="none" stroke="#fff" stroke-width="1.2"/></symbol>
    <symbol id="ico-person" viewBox="0 0 12 12"><circle cx="6" cy="6" r="5.3" fill="none" stroke="#8fc4f0" stroke-width="1"/><circle cx="6" cy="4.7" r="1.7" fill="#8fc4f0"/><path d="M3 9.2c.6-1.8 5.4-1.8 6 0z" fill="#8fc4f0"/></symbol>
    <symbol id="ico-phone" viewBox="0 0 12 12"><circle cx="6" cy="6" r="5.3" fill="none" stroke="#8fc4f0" stroke-width="1"/><path d="M4.2 3.3l1 1.3-.6.7c.4.9 1.1 1.6 2 2l.7-.6 1.3 1-.7 1C5.6 8.6 3.5 6.4 3.3 4z" fill="#8fc4f0"/></symbol>
    <symbol id="ico-mail" viewBox="0 0 12 12"><circle cx="6" cy="6" r="5.3" fill="none" stroke="#8fc4f0" stroke-width="1"/><rect x="3.3" y="4" width="5.4" height="4" fill="none" stroke="#8fc4f0" stroke-width=".9"/><path d="M3.3 4l2.7 2.2L8.7 4" fill="none" stroke="#8fc4f0" stroke-width=".9"/></symbol>
  </defs>
</svg>

<section class="flyer flyer--front">
  <div class="title-bar"></div>
  <h1 class="title">RECORD SALES</h1>
  <p class="address">4318 Heron Court,<br>La Jolla, CA</p>
  <p class="testimonial">Ned sold my oceanfront home in La Jolla and literally found the ‘needle- in-the-hay-stack’ cash buyer through his smart and targeted marketing backed by top notch Whitcombe Global Estates. He is an excellent communicator and negotiator and stays the course through thick and thin until a property is sold, while never losing focus on his #1 goal: to make his client happy. Definitely my agent of choice for any future transaction (buy or sell) and he should be yours too.</p>
  <div class="photo photo--hero" role="img" aria-label="Modern glass house lit at dusk" style="background:linear-gradient(160deg,#2e3a8a,#3b2f6b 55%,#5a3a2a)"></div>
  <aside class="highlights">
    <h2><span class="plain">The</span> Cedar<br>Loft</h2>
    <ul>
      <li><svg><use href="#tick"/></svg>4th Highest Sale in History of La Jolla’s Highly Desirable Fern Hollow Community</li>
      <li><svg><use href="#tick"/></svg>Recognized Internationally as a “One-of-a-Kind” Architectural Masterpiece</li>
      <li><svg><use href="#tick"/></svg>Featured on Real Estate TV Show “Coastal Prestige Homes”</li>
    </ul>
  </aside>
  <div class="photo photo--left" role="img" aria-label="Rooftop spa deck overlooking the ocean at sunset" style="background:linear-gradient(180deg,#e9dccb,#b49a82 60%,#6d5442)"></div>
  <div class="photo photo--right" role="img" aria-label="Glass-walled lounge with ocean view" style="background:linear-gradient(180deg,#4e7fb4,#34608f 60%,#7a5034)"></div>
  <div class="brand"><span class="group">Tidewell Group</span><span class="partner"><span class="divider"></span>Whitcombe Global Estates</span></div>
  <div class="contact-band"></div>
  <div class="contact">
    <div><svg><use href="#ico-person"/></svg>Ned Falworth</div>
    <div class="phone"><svg><use href="#ico-phone"/></svg>(858) 555-0172</div>
    <div><svg><use href="#ico-mail"/></svg>Ned@HOMQ-VT.example</div>
  </div>
</section>

<section class="flyer flyer--back">
  <div class="title-bar"></div>
  <h1 class="title">RECORD SALES</h1>
  <p class="address">3814 Vereda<br>Lumo, La Jolla, CA</p>
  <p class="testimonial">We feel so lucky and fortunate to have found Ned. He promised me he would handle our sale from beginning to the end. Not only did Ned keep his promise, he went above &amp; beyond to make sure the transaction stays at its course and time. Ned far exceeded our expectations in the price of the sale. I definitely will recommend Ned to all my family and friends. Thank you, Ned for an amazing experience.</p>
  <div class="photo photo--hero" role="img" aria-label="Balcony sofa with panoramic coastal view" style="background:linear-gradient(180deg,#9cc3e6,#5f8fb8 30%,#5f7a4a 55%,#8a7a64)"></div>
  <aside class="highlights">
    <h2>Marisol<br>Heights</h2>
    <ul>
      <li><svg><use href="#tick"/></svg>2nd Highest Sale Price</li>
      <li><svg><use href="#tick"/></svg>3rd Highest Price Per S/F since 1997</li>
      <li><svg><use href="#tick"/></svg>Extensive Pre-MLS Marketing. Sold on Day 1 of Listing</li>
    </ul>
  </aside>
  <div class="photo photo--left" role="img" aria-label="Bright bedroom with garden views" style="background:linear-gradient(180deg,#d8d3c8,#b8b0a0 60%,#8c8478)"></div>
  <div class="photo photo--right" role="img" aria-label="Wood kitchen and dining area" style="background:linear-gradient(180deg,#d9cfc0,#b0885e 55%,#7a5634)"></div>
  <div class="brand"><span class="group">Tidewell Group</span><span class="partner"><span class="divider"></span>Whitcombe Global Estates</span></div>
  <div class="contact-band"></div>
  <div class="contact">
    <div><svg><use href="#ico-person"/></svg>Ned Falworth</div>
    <div class="phone"><svg><use href="#ico-phone"/></svg>(858) 555-0172</div>
    <div><svg><use href="#ico-mail"/></svg>Ned@HOMQ-VT.example</div>
  </div>
</section>

</body>
</html>
```